Medical Cannabis company is looking for a LOGO design *

SILVER PETALWORKS (SP) is a new company in the Israeli medical cannabis industry. We will engage in PREMIUM medical cannabis growing and cultivation and also manufacturing of HIGH-END cannabis based medical products.
the design should reflect luxury, high-end and Pharma-grade products.
the design should use color GOLD and NOT using the famous cannabis leaf !

Target Market(s)

international medical cannabis Pharmaceutical companies
and of course local and international patients

Contact Information for Business Card

Yoav Ben-Ami
Founder and CEO

Silver Petalworks
Medical grade cannabis

yoavbenami@mailnest.example
972-52-3186907

Colors
ffc214
fbed22

Requirements
Must have
• clean and simple
• luxury
• gold !!
• (can also have green for Cannabis and/or blue for Pharma)
Should not have
• cannabis leaf

```html
<!DOCTYPE html>
<html lang="en">
<head>
<meta charset="utf-8">
<title>Silver Petalworks — Business Card</title>
<link rel="stylesheet" href="https://fonts.googleapis.com/css2?family=Orbitron:wght@400&family=Great+Vibes&family=Open+Sans:wght@400&display=swap">
<style>
  :root {
    --gold-deep: #9a5e0d;
    --gold-mid: #c8961a;
    --gold-bright: #fbe322;
    --gold-text: #d9a31c;
    --ink: #000000;
    --muted: #1e1e1e;
    --rule: #222222;
  }
  * { margin: 0; padding: 0; box-sizing: border-box; }
  html, body { width: 1200px; height: 1200px; overflow: hidden; }
  body {
    position: relative;
    background: linear-gradient(135deg, var(--gold-deep) 0%, var(--gold-mid) 30%, var(--gold-bright) 50%, var(--gold-mid) 70%, var(--gold-deep) 100%);
    font-family: "Open Sans", sans-serif;
  }
  .flourish {
    position: absolute;
    width: 90px;
    height: 450px;
    background: radial-gradient(ellipse 50% 50% at 50% 50%, rgba(74,38,10,0.28) 0%, rgba(74,38,10,0.12) 55%, rgba(74,38,10,0) 100%);
  }
  .flourish--top-left { left: 12px; top: 12px; }
  .flourish--bottom-right { left: 1106px; top: 728px; }

  .card {
    position: absolute;
    width: 840px;
    height: 480px;
    background: var(--ink);
    overflow: hidden;
  }
  .card--front { left: 203px; top: 102px; }
  .card--back { left: 198px; top: 642px; }

  .front-accent {
    position: absolute;
    width: 90px;
    background: radial-gradient(ellipse 50% 50% at 50% 50%, rgba(217,163,28,0.22) 0%, rgba(217,163,28,0.06) 60%, rgba(217,163,28,0) 100%);
  }
  .front-accent--left { left: 0; top: 0; height: 390px; }
  .front-accent--right { right: 0; top: 110px; height: 370px; }

  .brand-name {
    position: absolute;
    left: 0; right: 0;
    top: 196px;
    text-align: center;
    font-family: "Orbitron", sans-serif;
    font-weight: 400;
    font-size: 34px;
    line-height: 40px;
    letter-spacing: 1px;
    color: var(--gold-text);
    padding-left: 20px;
  }
  .brand-rule {
    position: absolute;
    left: 99px; width: 642px;
    top: 262px; height: 5px;
    background: linear-gradient(90deg, var(--gold-deep), var(--gold-bright) 50%, var(--gold-deep));
  }

  .back-spine {
    position: absolute;
    left: 0; top: 0; bottom: 0;
    width: 30px;
    background: var(--ink);
    border-right: 2px solid var(--gold-mid);
  }
  .back-spine::before {
    content: "";
    position: absolute;
    left: 20px; top: 0; bottom: 0;
    width: 1px;
    background: #3a3a3a;
  }
  .name-band {
    position: absolute;
    left: 31px; right: 0; top: 0;
    height: 190px;
    background: linear-gradient(90deg, var(--gold-deep) 0%, var(--gold-mid) 30%, var(--gold-bright) 57%, var(--gold-mid) 80%, var(--gold-deep) 100%);
    border-bottom: 2px solid #b56d0e;
    text-align: center;
  }
  .person-name {
    font-family: "Great Vibes", cursive;
    font-weight: 400;
    font-size: 86px;
    line-height: 1;
    color: var(--ink);
    padding-top: 48px;
    text-shadow: 0 0 1px var(--ink);
  }
  .person-role {
    font-size: 22px;
    color: var(--ink);
    margin-top: 4px;
  }
  .contact {
    position: absolute;
    left: 60px;
    display: flex;
    align-items: center;
    font-size: 27px;
    color: var(--gold-text);
  }
  .contact svg { width: 30px; height: 30px; margin-right: 42px; }
  .contact--email { top: 276px; }
  .contact--phone { top: 334px; }
  .contact-rule {
    position: absolute;
    left: 74px; width: 715px;
    top: 391px; height: 1px;
    background: var(--rule);
  }
  .company-footer {
    position: absolute;
    left: 31px; right: 0;
    top: 408px;
    text-align: center;
    font-size: 19px;
    line-height: 25px;
    color: var(--muted);
  }
</style>
</head>
<body>
  <div class="flourish flourish--top-left" role="img" aria-label="Flowing vine flourish with dotted accents"></div>
  <div class="flourish flourish--bottom-right" role="img" aria-label="Flowing vine flourish with dotted accents"></div>

  <section class="card card--front">
    <div class="front-accent front-accent--left" role="img" aria-label="Gold swirl ornament"></div>
    <div class="front-accent front-accent--right" role="img" aria-label="Gold swirl ornament"></div>
    <h1 class="brand-name">SILVER PETALWORKS</h1>
    <div class="brand-rule"></div>
  </section>

  <section class="card card--back">
    <div class="back-spine"></div>
    <header class="name-band">
      <h2 class="person-name">Yoav Ben-Ami</h2>
      <p class="person-role">Founder and CEO</p>
    </header>

    <p class="contact contact--email">
      <svg viewBox="0 0 30 30" aria-hidden="true">
        <rect x="2" y="7" width="26" height="17" fill="none" stroke="#d9a31c" stroke-width="2"/>
        <path d="M2 7 L15 17 L28 7 M2 24 L12 15 M28 24 L18 15" fill="none" stroke="#d9a31c" stroke-width="1.6"/>
      </svg>
      yoavbenami@mailnest.example
    </p>
    <p class="contact contact--phone">
      <svg viewBox="0 0 30 30" aria-hidden="true">
        <path d="M6 3 L11 3 L13 10 L10 12 C 11 16, 14 19, 18 21 L20 18 L27 20 L27 25 C 20 29, 3 17, 6 3 Z" fill="#d9a31c"/>
      </svg>
      972-52-3186907
    </p>
    <div class="contact-rule"></div>
    <p class="company-footer">Silver Petalworks<br>Medical grade cannabis</p>
  </section>
</body>
</html>
```